Kelbrook LLC web design project

Dallas, TX based water damage mitigation company needs a web site for its new business. The company does water extractions, mitigation, demo, restoration, and reconstruction. We need for the site to have a strong mobile version, and the owners/managers need to be able to edit the site despite having no web design experience. The site needs to look and function, especially the mobile version, similar to bramfieldorchardworks.com if possible.

```html
<!DOCTYPE html>
<html lang="en">
<head>
<meta charset="utf-8">
<title>Kelbrook LLC – Water Damage Mitigation</title>
<link rel="stylesheet" href="https://fonts.googleapis.com/css2?family=Montserrat:wght@400;500;600;700&family=Source+Sans+3:wght@400;600&display=swap">
<style>
:root{
  --slate:#3c4a59;
  --grey:#6e7f92;
  --blue:#0077c0;
  --blue-soft:#1a86cc;
  --canvas:#eeeff1;
  --white:#ffffff;
  --text:#5b6673;
  --line:#e3e6ea;
}
*{box-sizing:border-box;margin:0;padding:0}
html,body{width:1200px;height:3718px;overflow:hidden}
body{background:var(--canvas);font-family:"Source Sans 3",sans-serif;color:var(--text);position:relative}
.abs{position:absolute}

/* style guide header */
.brand{left:302px;top:118px;width:130px;text-align:center}
.brand-dot{width:28px;height:28px;border-radius:50%;background:var(--slate);margin:0 auto 6px}
.brand-name{font-family:"Montserrat",sans-serif;font-weight:600;font-size:21px;color:var(--slate);letter-spacing:.5px}
.guide-rule{top:94px;width:1px;height:84px;background:#c9ced4}
.guide-title{font-family:"Montserrat",sans-serif;font-size:21px;color:var(--slate);font-weight:500}
.font-list{left:546px;top:92px}
.font-list .f1{font-family:"Montserrat",sans-serif;font-size:17px;margin-top:18px;color:var(--grey)}
.font-list .f2{font-size:15px;margin-top:6px;color:var(--grey)}
.swatches{left:764px;top:92px}
.swatch-row{display:flex;gap:10px;margin-top:10px}
.swatch{text-align:center;font-size:8px;color:var(--grey)}
.swatch i{display:block;width:36px;height:36px;border-radius:50%;margin-bottom:5px}

/* page */
.page{left:347px;top:826px;width:507px;height:2801px;background:var(--white);overflow:hidden;box-shadow:0 4px 20px rgba(0,0,0,.05)}
.section{position:absolute;left:0;width:507px}
.h-title{font-family:"Montserrat",sans-serif;font-weight:600;font-size:10.5px;color:var(--slate);letter-spacing:.2px;text-align:center}
.txt{font-size:5px;line-height:1.75;color:var(--text)}
.rule{position:absolute;left:68px;width:371px;height:1px;background:var(--line)}

/* hero */
.hero{top:0;height:286px;background:linear-gradient(180deg,#e9ecef 0%,#d7dde2 45%,#b9c2c9 75%,#9aa7b2 100%)}
.hero-menu{left:68px;top:35px;font-family:"Montserrat",sans-serif;font-size:7px;color:var(--blue);font-weight:600}
.hero-menu span{display:inline-block;width:10px;height:5px;border-top:1px solid var(--blue);border-bottom:1px solid var(--blue);vertical-align:middle;margin-left:3px;position:relative}
.hero-logo{left:203px;top:32px;width:100px;text-align:center}
.hero-logo .dot{width:14px;height:14px;border-radius:50%;background:var(--slate);margin:0 auto 3px}
.hero-logo .name{font-family:"Montserrat",sans-serif;font-weight:600;font-size:9px;color:var(--slate)}
.hero-call{left:370px;top:20px;width:70px;text-align:center;font-size:4.5px;color:var(--blue)}
.hero-call .pill{margin:3px 0;height:15px;border-radius:8px;background:var(--slate);color:#fff;font-size:5px;display:flex;align-items:center;justify-content:center;gap:4px}
.hero-call .pill i{width:9px;height:9px;border-radius:50%;background:#fff;display:inline-block}
.hero-banner{left:68px;top:260px;width:371px;height:50px;border-radius:25px;background:var(--blue);color:#fff;font-family:"Montserrat",sans-serif;font-weight:600;font-size:11px;display:flex;align-items:center;justify-content:center;letter-spacing:.3px;z-index:2}

/* services */
.svc-card{position:absolute;top:495px;width:86px;height:205px;background:#fff;box-shadow:0 1px 5px rgba(0,0,0,.1);padding:7px 6px}
.svc-label{border:1px solid #c8cdd3;font-size:4.5px;text-align:center;padding:3px 0;text-transform:uppercase;color:var(--slate)}
.svc-photo{height:57px;margin-top:7px}
.svc-list{list-style:none;margin-top:9px;font-size:4.5px;line-height:2.45;padding-left:6px}
.svc-list li::before{content:"✓ ";color:var(--slate)}
.svc-btn{position:absolute;left:6px;right:6px;bottom:7px;height:17px;border-radius:9px;background:var(--blue);color:#fff;font-size:4.5px;font-weight:600;display:flex;align-items:center;justify-content:center}

/* pricing */
.pricing{top:742px;height:227px;background:var(--slate)}
.pricing .h-title{color:#fff;position:absolute;top:37px;width:100%}
.price-item{position:absolute;width:120px;font-size:4.5px;line-height:1.7;color:#c9d1da}
.price-item b{display:block;font-family:"Montserrat",sans-serif;font-size:5px;color:#fff;font-weight:600}
.price-icon{position:absolute;width:14px;height:14px;border:1.2px solid #dfe4ea;border-radius:3px}
.price-logo{left:198px;top:102px;width:111px;text-align:center}
.price-logo .dot{width:40px;height:40px;border-radius:50%;background:#fff;margin:0 auto 6px}
.price-logo .name{font-family:"Montserrat",sans-serif;font-weight:600;font-size:16px;color:#fff}

/* equipment intro */
.equip-title{left:68px;top:1060px;font-family:"Montserrat",sans-serif;font-weight:600;font-size:11px;color:var(--slate);line-height:1.35}
.equip-photo{left:288px;top:980px;width:152px;height:222px;border-radius:0 0 76px 76px;background:linear-gradient(200deg,#eef0f2 0%,#d5dbe2 45%,#3f5f9a 75%,#2a3a55 100%)}

/* compare */
.bar-label{font-size:4.5px;color:var(--slate);text-transform:uppercase}
.bar{position:absolute;height:11px;border-radius:6px;font-size:4px;color:#fff;display:flex;align-items:center;justify-content:space-between;padding:0 5px}
.bar-track{position:absolute;height:11px;border-radius:6px;background:#e9edf1}
.dehum{left:225px;top:1315px;width:54px;height:105px;border-radius:8px;background:linear-gradient(180deg,#2f84d2,#0a4f9b)}

/* estimate */
.van{left:47px;top:1512px;width:200px;height:170px;background:radial-gradient(ellipse at 55% 55%,#3b4558 0%,#5a6577 45%,#e9ecef 72%,#fff 80%)}
.est-title{left:258px;top:1505px;font-family:"Montserrat",sans-serif;font-weight:600;font-size:11px;color:var(--slate);line-height:1.35}
.est-sub{left:258px;top:1541px;font-size:5px;color:var(--grey)}
.est-row{position:absolute;left:258px;width:181px}
.est-row b{font-family:"Montserrat",sans-serif;font-size:5px;color:var(--blue);font-weight:600}
.est-row .txt{width:120px}
.est-btn{position:absolute;right:0;top:3px;width:53px;height:17px;border-radius:9px;color:#fff;font-size:4.5px;font-weight:600;display:flex;align-items:center;justify-content:center}

/* why */
.why{top:1727px;height:339px;background:var(--blue-soft)}
.why .h-title{color:#fff;position:absolute;top:40px;width:100%}
.why-panel{position:absolute;left:68px;top:72px;width:371px;height:227px;background:#2f92d4}
.why-item{position:absolute;width:140px;font-size:4.5px;line-height:1.7;color:#d7ebf8;padding-left:22px}
.why-item b{display:block;font-family:"Montserrat",sans-serif;font-size:5px;color:#fff;font-weight:600}
.why-item i{position:absolute;left:0;top:2px;width:14px;height:14px;border:1.2px solid #fff;border-radius:50%}

/* areas */
.area-title{left:68px;top:2114px;font-family:"Montserrat",sans-serif;font-weight:600;font-size:11px;color:var(--slate)}
.area-list{left:68px;top:2188px;display:grid;grid-template-columns:50px 50px;font-size:4.5px;line-height:2.3}
.area-list span::before{content:"";display:inline-block;width:4px;height:4px;border-radius:50%;background:var(--blue);margin-right:3px}
.map{left:275px;top:2106px;width:166px;height:166px;border-radius:50%;background:linear-gradient(135deg,#f4f5f7,#e6e9ed)}
.map-pin{left:275px;top:2235px;width:34px;height:34px;border-radius:50%;background:var(--slate)}

/* cta */
.cta{left:68px;top:2312px;width:371px;height:64px;border-radius:32px;background:var(--blue);color:#fff;font-family:"Montserrat",sans-serif;padding:18px 0 0 22px}
.cta .l1{font-size:8px;letter-spacing:.6px;font-weight:400}
.cta .l2{font-size:9px;font-weight:700;margin-top:2px}
.cta-btn{position:absolute;right:22px;top:23px;width:56px;height:18px;border-radius:9px;background:#fff;color:var(--blue);font-size:4.5px;font-weight:700;display:flex;align-items:center;justify-content:center}

/* reviews */
.review{position:absolute;top:2447px;width:116px;height:91px;background:#f4f5f7;padding:8px}
.review .who{display:flex;gap:4px;align-items:center;font-size:4.5px;color:var(--slate);font-weight:600}
.review .who i{width:10px;height:10px;border-radius:50%;background:#3d8a3a}
.review .stars{color:#f4b400;font-size:6px;margin:3px 0}
.rev-note{left:0;top:2555px;width:507px;text-align:center;font-size:4.5px}
.rev-note a{display:block;color:var(--blue);text-decoration:underline;margin-top:5px}

/* footer */
.footer{top:2615px;height:186px;background:var(--slate);color:#c9d1da}
.foot-brand{left:68px;top:60px;width:90px;text-align:center}
.foot-brand .dot{width:26px;height:26px;border-radius:50%;background:#fff;margin:0 auto 5px}
.foot-brand .name{font-family:"Montserrat",sans-serif;font-weight:600;font-size:13px;color:#fff}
.foot-col{position:absolute;top:44px;font-size:4.5px;line-height:2.4}
.foot-col b{display:block;font-family:"Montserrat",sans-serif;font-size:6px;color:#fff;margin-bottom:4px}
.foot-copy{left:0;top:165px;width:507px;text-align:center;font-size:4.5px}
</style>
</head>
<body>

<!-- style guide -->
<div class="abs brand"><div class="brand-dot"></div><div class="brand-name">KELBROOK LLC</div></div>
<div class="abs guide-rule" style="left:488px"></div>
<div class="abs font-list"><div class="guide-title">Fonts:</div><div class="f1">Montserrat</div><div class="f2">Source Sans Pro</div></div>
<div class="abs guide-rule" style="left:705px"></div>
<div class="abs swatches"><div class="guide-title">Colors:</div>
  <div class="swatch-row">
    <div class="swatch"><i style="background:var(--slate)"></i>#3c4a59</div>
    <div class="swatch"><i style="background:var(--grey)"></i>#6e7f92</div>
    <div class="swatch"><i style="background:var(--blue)"></i>#0077c0</div>
  </div>
</div>

<!-- page -->
<main class="abs page">

  <section class="section hero" role="img" aria-label="Photo of a room with air movers and dehumidifiers drying out water damage"></section>
  <div class="abs hero-menu">MENU<span></span></div>
  <div class="abs hero-logo"><div class="dot"></div><div class="name">KELBROOK LLC</div></div>
  <div class="abs hero-call">CLICK TO CALL<div class="pill"><i></i>+1 555 014 2290</div>MON - SAT, 8 AM TO 6 PM</div>
  <div class="abs hero-banner">WATER DAMAGE MITIGATION SPECIALISTS</div>

  <p class="abs txt" style="left:68px;top:351px;width:145px">We respond fast to floods, leaks and burst pipes across the metro area. Our certified crew extracts water, dries every room and keeps you informed from first call to final walkthrough.</p>
  <p class="abs txt" style="left:289px;top:351px;width:150px">Every job starts with moisture mapping and a clear written plan. We use commercial drying gear and document progress daily so your insurer sees the whole picture.</p>
  <div class="rule" style="top:430px"></div>

  <div class="abs h-title" style="top:468px;width:507px">- OUR SERVICES -</div>
  <div class="svc-card" style="left:68px"><div class="svc-label">Water Extraction</div><div class="svc-photo" role="img" aria-label="Photo of water extraction hoses on a floor" style="background:linear-gradient(135deg,#3c6fb0,#8a9bb0)"></div>
    <ul class="svc-list"><li>Fast site response</li><li>Standing water removal</li><li>Carpet extraction</li><li>Pad assessment</li><li>Moisture readings</li><li>Photo reports</li></ul><div class="svc-btn">EXPLORE SERVICE →</div></div>
  <div class="svc-card" style="left:163px"><div class="svc-label">Mitigation</div><div class="svc-photo" role="img" aria-label="Photo of an air mover on a wet floor" style="background:linear-gradient(135deg,#1c5ea8,#8597ad)"></div>
    <ul class="svc-list"><li>Air mover setup</li><li>Dehumidification</li><li>Containment walls</li><li>Mold prevention</li><li>Daily monitoring</li><li>Drying logs</li></ul><div class="svc-btn">EXPLORE SERVICE →</div></div>
  <div class="svc-card" style="left:258px"><div class="svc-label">Restoration</div><div class="svc-photo" role="img" aria-label="Photo of drying equipment in a home" style="background:linear-gradient(135deg,#2a5fa0,#b7c0ca)"></div>
    <ul class="svc-list"><li>Drywall repair</li><li>Floor replacement</li><li>Cabinet repair</li><li>Paint and trim</li><li>Odor control</li><li>Final cleaning</li></ul><div class="svc-btn">EXPLORE SERVICE →</div></div>
  <div class="svc-card" style="left:353px"><div class="svc-label">Reconstruction</div><div class="svc-photo" role="img" aria-label="Photo of a room under reconstruction" style="background:linear-gradient(135deg,#3f8fd0,#cfd8e0)"></div>
    <ul class="svc-list"><li>Full rebuilds</li><li>Framing work</li><li>Insulation</li><li>Tile and flooring</li><li>Permit handling</li><li>Walkthrough</li></ul><div class="svc-btn">EXPLORE SERVICE →</div></div>

  <section class="section pricing">
    <div class="h-title">- HOW WE PRICE -</div>
    <i class="price-icon" style="left:68px;top:68px"></i>
    <div class="price-item" style="left:92px;top:67px"><b>FREE ESTIMATES</b>We inspect the damage and quote before any work begins.</div>
    <i class="price-icon" style="left:68px;top:111px"></i>
    <div class="price-item" style="left:92px;top:110px"><b>VOLUME BASED PRICING</b>Our pricing depends on the amount of damage that has been found.</div>
    <i class="price-icon" style="left:68px;top:155px"></i>
    <div class="price-item" style="left:92px;top:154px"><b>NO HIDDEN FEES</b>All labor, equipment and disposal fees are included in your quote.</div>
    <i class="price-icon" style="left:425px;top:68px"></i>
    <div class="price-item" style="left:298px;top:67px;text-align:right"><b>MINIMUM LOADS</b>Small jobs are welcome, with a fair minimum charge for every visit.</div>
    <i class="price-icon" style="left:425px;top:111px"></i>
    <div class="price-item" style="left:298px;top:110px;text-align:right"><b>UPFRONT PRICING</b>We always give you the price with a firm quote before we begin.</div>
    <i class="price-icon" style="left:425px;top:155px"></i>
    <div class="price-item" style="left:298px;top:154px;text-align:right"><b>BETTER VALUE</b>Our rates beat national franchises while keeping local care.</div>
    <div class="abs price-logo"><div class="dot"></div><div class="name">KELBROOK LLC</div></div>
  </section>

  <div class="abs equip-title">- DECENT EQUIPMENTS,<br>DECENT RESULTS! -</div>
  <p class="abs txt" style="left:68px;top:1091px;width:148px">Our trucks carry commercial extractors, low grain dehumidifiers and high velocity air movers. Better tools mean shorter drying times and fewer repairs.</p>
  <p class="abs txt" style="left:68px;top:1136px;width:148px">Each unit is serviced between jobs so it runs at full capacity in your home.</p>
  <div class="abs equip-photo" role="img" aria-label="Photo of a technician inspecting a ceiling duct"></div>
  <div class="rule" style="top:1241px"></div>

  <div class="abs h-title" style="top:1280px;width:507px">- OUR EQUIPMENT VS COMPETITORS -</div>
  <div class="abs bar-label" style="left:68px;top:1325px">Our Equipment</div>
  <div class="bar" style="left:68px;top:1346px;width:112px;background:var(--blue)"><span>Clean Complex Areas</span><span>95%</span></div>
  <div class="bar" style="left:68px;top:1366px;width:112px;background:var(--grey)"><span>Dryness</span><span>98%</span></div>
  <div class="bar" style="left:68px;top:1386px;width:112px;background:var(--slate)"><span>Clean Complex Areas</span><span>95%</span></div>
  <div class="abs dehum" role="img" aria-label="Photo of a blue commercial dehumidifier"></div>
  <div class="abs bar-label" style="left:313px;top:1325px">Competitors Equipment</div>
  <div class="bar-track" style="left:313px;top:1346px;width:116px"></div><div class="bar" style="left:313px;top:1346px;width:72px;background:var(--blue)"><span>Clean Complex Areas</span><span>60%</span></div>
  <div class="bar-track" style="left:313px;top:1366px;width:116px"></div><div class="bar" style="left:313px;top:1366px;width:72px;background:var(--grey)"><span>Dryness</span><span>60%</span></div>
  <div class="bar-track" style="left:313px;top:1386px;width:116px"></div><div class="bar" style="left:313px;top:1386px;width:72px;background:var(--slate)"><span>Clean Complex Areas</span><span>60%</span></div>
  <div class="rule" style="top:1462px"></div>

  <div class="abs van" role="img" aria-label="Photo of a technician with a clipboard in front of a service van"></div>
  <div class="abs est-title">3 SIMPLE WAYS TO GET YOUR<br>ESTIMATE TODAY!</div>
  <div class="abs est-sub">Fast, Friendly, Professional, Reliable</div>
  <div class="est-row" style="top:1574px"><b>CALL US</b><p class="txt">Call us today and talk to one of our friendly team about your damage.</p><div class="est-btn" style="background:var(--blue)">CLICK TO CALL</div></div>
  <div class="est-row" style="top:1616px"><b>TEXT US</b><p class="txt">Text us a few photos of the damage so we can prepare your estimate.</p><div class="est-btn" style="background:var(--grey)">CLICK TO TEXT</div></div>
  <div class="est-row" style="top:1658px"><b>EMAIL US</b><p class="txt">Email us the details and photos and we will reply with an estimate.</p><div class="est-btn" style="background:var(--slate)">CLICK TO MAIL</div></div>

  <section class="section why">
    <div class="h-title">- WHY CHOOSING KELBROOK? -</div>
    <div class="why-panel">
      <div class="why-item" style="left:22px;top:24px"><i></i><b>EASY SCHEDULING</b>Call, text or email and we will book a visit at the time that suits you best.</div>
      <div class="why-item" style="left:200px;top:24px"><i></i><b>UPFRONT PRICING</b>We explain the scope and cost of every step before we start working.</div>
      <div class="why-item" style="left:22px;top:90px"><i></i><b>PROFESSIONAL SERVICE</b>Our certified technicians arrive on time, in uniform and ready to work.</div>
      <div class="why-item" style="left:200px;top:90px"><i></i><b>ALL CLEANED UP</b>We remove all equipment and debris and leave every room clean and tidy.</div>
      <div class="why-item" style="left:22px;top:156px"><i></i><b>EXCELLENT COMMUNICATION</b>We share daily progress updates and answer your questions quickly.</div>
      <div class="why-item" style="left:200px;top:156px"><i></i><b>EASY PAYMENT METHODS</b>Pay by card, check or transfer, and we work directly with your insurer.</div>
    </div>
  </section>

  <div class="abs area-title">- WORKING AREAS -</div>
  <p class="abs txt" style="left:68px;top:2140px;width:160px">Kelbrook LLC offers water extractions, mitigation, demo, restoration and reconstruction across the greater Dallas area. Contact us if your area is not listed below and we will gladly help.</p>
  <div class="abs area-list"><span>Plano</span><span>Garland</span><span>Irving</span><span>Frisco</span><span>Mesquite</span><span>Allen</span><span>Arlington</span><span>Carrollton</span></div>
  <div class="abs map" role="img" aria-label="Map of the service area around Dallas"></div>
  <div class="abs map-pin"><svg width="34" height="34" viewBox="0 0 34 34"><path d="M17 9a6 6 0 0 0-6 6c0 4.5 6 10 6 10s6-5.5 6-10a6 6 0 0 0-6-6zm0 8.2a2.2 2.2 0 1 1 0-4.4 2.2 2.2 0 0 1 0 4.4z" fill="#fff"/></svg></div>

  <div class="abs cta"><div class="l1">WE OFFER SAME &amp; NEXT DAY SERVICE.</div><div class="l2">SCHEDULE YOUR APPOINTMENT NOW!</div><div class="cta-btn">CONTACT US</div></div>

  <div class="abs h-title" style="top:2416px;width:507px">- CLIENT REVIEWS -</div>
  <div class="review" style="left:68px"><div class="who"><i></i>Marta Ellison</div><div class="stars">★★★★★</div><p class="txt">The crew arrived within an hour, dried our kitchen in three days and kept us updated the whole time. Highly recommended.</p></div>
  <div class="review" style="left:195px"><div class="who"><i></i>Marta Ellison</div><div class="stars">★★★★★</div><p class="txt">Honest pricing and friendly technicians. They handled the insurance paperwork and left the house spotless.</p></div>
  <div class="review" style="left:322px"><div class="who"><i></i>Marta Ellison</div><div class="stars">★★★★★</div><p class="txt">A burst pipe flooded our basement and they had it dry and rebuilt quickly. Great communication throughout.</p></div>
  <div class="abs rev-note">Our clients rate us 4.9 of 5 based on 96 reviews<a>CLICK HERE TO READ MORE REVIEWS</a></div>

  <footer class="section footer">
    <div class="abs foot-brand"><div class="dot"></div><div class="name">KELBROOK LLC</div></div>
    <div class="foot-col" style="left:198px"><b>LINKS</b>› Home<br>› Services<br>› How We Price<br>› Areas<br>› Reviews<br>› Contact</div>
    <div class="foot-col" style="left:278px"><b>SERVICES</b>› Water Extraction<br>› Mitigation<br>› Demo<br>› Restoration<br>› Reconstruction</div>
    <div class="foot-col" style="left:365px"><b>CONTACT US</b>
      <svg width="10" height="10" viewBox="0 0 10 10" style="vertical-align:middle"><circle cx="5" cy="5" r="4.5" fill="none" stroke="#c9d1da" stroke-width=".8"/></svg> Call Us: +1 555 014 2290<br><br>
      <svg width="10" height="10" viewBox="0 0 10 10" style="vertical-align:middle"><circle cx="5" cy="5" r="4.5" fill="none" stroke="#c9d1da" stroke-width=".8"/></svg> Mon - Sat, 8 AM to 6 PM</div>
    <div class="abs foot-copy">Copyright 2024 KELBROOK LLC - All Rights Reserved</div>
  </footer>
</main>
</body>
</html>
```